Design a Professional Business Card for Velmora Arcs

Design a business card for Velmora Arcs, we are a National Sport Court Company.

West Region Address: 4175 Quill Harbor Ln, Suite #215 Haddon Ridge, Corrander 80467
East Region Address: 3817 Tamsin Rd E, Larkspur Point, Marisol 34583

Target Market(s)

High End Residential & Institutional Clients

Industry/Entity Type

Design & Construction

Contact Information for Business Card

Logo/Brand/Colors/ name, number (provided in comments)

Requirements
Must have
• Colors only provided in logo
Should not have
• Any other colors not in existing logo (attached)

```html
<!DOCTYPE html>
<html lang="en">
<head>
<meta charset="utf-8">
<title>Velmora Arcs – Business Card</title>
<link rel="stylesheet" href="https://fonts.googleapis.com/css2?family=Poppins:wght@400;500;600;700&display=swap">
<style>
  :root {
    --brand-blue: #1f4f9a;
    --brand-blue-deep: #163d7c;
    --brand-green: #1fa04a;
    --paper: #ffffff;
    --paper-shade: #eef0f3;
    --stage: #e7e5e1;
    --ink-light: #ffffff;
  }
  * { margin: 0; padding: 0; box-sizing: border-box; }
  html, body { width: 1200px; height: 1027px; overflow: hidden; }
  body {
    background: var(--stage);
    font-family: "Poppins", sans-serif;
    display: flex;
    flex-direction: column;
    align-items: center;
    justify-content: center;
    gap: 30px;
  }
  .card {
    position: relative;
    width: 840px;
    height: 470px;
    border-radius: 22px;
    overflow: hidden;
    background: linear-gradient(180deg, var(--paper), var(--paper-shade));
    box-shadow: 0 10px 28px rgba(0,0,0,0.18);
  }
  .card__shape { position: absolute; inset: 0; }
  .brand {
    position: absolute;
    display: flex;
    align-items: center;
    gap: 18px;
    color: var(--brand-blue);
    font-weight: 700;
    text-transform: uppercase;
    letter-spacing: 3px;
    white-space: nowrap;
    line-height: 1;
  }
  .card--front .brand { top: 72px; left: 50%; transform: translateX(-50%); font-size: 40px; }
  .card--back .brand { top: 50%; left: 50%; transform: translate(-50%, -50%); font-size: 58px; }
  .brand__dot {
    width: 0.95em; height: 0.95em; border-radius: 50%;
    background: var(--brand-green);
    flex: none;
  }
  .details {
    position: absolute;
    left: 56px; right: 56px; bottom: 44px;
    display: flex;
    justify-content: space-between;
    color: var(--ink-light);
  }
  .person__name { font-size: 27px; font-weight: 600; letter-spacing: 1px; text-transform: uppercase; line-height: 1.1; }
  .person__role { font-size: 19px; font-weight: 400; margin-bottom: 22px; }
  .contact { list-style: none; font-size: 17px; line-height: 1.8; }
  .contact li { display: flex; align-items: center; gap: 12px; }
  .contact svg { width: 20px; height: 20px; flex: none; }
  .region { font-size: 16px; line-height: 1.45; margin-bottom: 14px; }
  .region:last-child { margin-bottom: 0; }
  .region__label { font-weight: 700; font-size: 14px; letter-spacing: 0.5px; text-transform: uppercase; }
</style>
</head>
<body>

  <section class="card card--front" aria-label="Business card front">
    <svg class="card__shape" viewBox="0 0 840 470" preserveAspectRatio="none" aria-hidden="true">
      <defs>
        <linearGradient id="blueBand" x1="0" y1="0" x2="1" y2="1">
          <stop offset="0" stop-color="#2458a8"/>
          <stop offset="1" stop-color="#163d7c"/>
        </linearGradient>
      </defs>
      <path d="M0,170 Q420,300 840,170 L840,186 Q420,316 0,186 Z" fill="var(--brand-green)"/>
      <path d="M0,192 Q420,322 840,192 L840,470 L0,470 Z" fill="url(#blueBand)"/>
    </svg>

    <div class="brand"><span class="brand__dot"></span>Velmora Arcs</div>

    <div class="details">
      <div class="person">
        <div class="person__name">Dorian Kessler</div>
        <div class="person__role">Manager</div>
        <ul class="contact">
          <li>
            <svg viewBox="0 0 20 20"><circle cx="10" cy="10" r="10" fill="#fff"/><path d="M7 5h2l1 3-1.5 1a6 6 0 0 0 2.5 2.5L12 10l3 1v2a1 1 0 0 1-1 1A9 9 0 0 1 6 6a1 1 0 0 1 1-1z" fill="var(--brand-blue)"/></svg>
            555-214-0387
          </li>
          <li>
            <svg viewBox="0 0 20 20"><circle cx="10" cy="10" r="10" fill="#fff"/><rect x="5" y="6.5" width="10" height="7" rx="1" fill="var(--brand-blue)"/><path d="M5.5 7l4.5 3.5L14.5 7" stroke="#fff" stroke-width="1" fill="none"/></svg>
            hello@velmoraarcs.com
          </li>
        </ul>
      </div>
      <div class="regions">
        <div class="region">
          <div class="region__label">East Region Address</div>
          3817 Tamsin Rd E, Larkspur Point,<br>Marisol 34583
        </div>
        <div class="region">
          <div class="region__label">West Region Address</div>
          4175 Quill Harbor Ln, Suite #215<br>Haddon Ridge, Corrander 80467
        </div>
      </div>
    </div>
  </section>

  <section class="card card--back" aria-label="Business card back">
    <div class="brand"><span class="brand__dot"></span>Velmora Arcs</div>
  </section>

</body>
</html>
```